Valbrook Data Works

Our company is about IT hardwares and IT solutions. IT hardware such as PC, RAMS, storage and servers. IT solutions such as project management, BA. We are also selling new technology too.

Target Market(s)

Consumer, Small to Medium Business, Corporate

Requirements
Must have
• The business card must have the following:
• Name:
• Title:
• Contact Number:
• Email address:
• Website:
• Color: Must match the logo color upgrade

```html
<!DOCTYPE html>
<html lang="en">
<head>
<meta charset="utf-8">
<title>Valbrook Data Works – Business Card</title>
<link href="https://fonts.googleapis.com/css2?family=Michroma&family=Open+Sans:wght@400;600&display=swap" rel="stylesheet">
<style>
  :root {
    --stage: #2b2b2b;
    --card-dark: #3a3a3b;
    --card-dark-deep: #2c2c2d;
    --card-light: #ffffff;
    --ink: #3b3b3d;
    --accent: #d9892a;
    --muted: #4a4a4a;
  }
  * { margin: 0; padding: 0; box-sizing: border-box; }
  html, body { width: 1200px; height: 904px; overflow: hidden; }
  body {
    background: var(--stage);
    position: relative;
    font-family: "Open Sans", sans-serif;
  }
  .card {
    position: absolute;
    width: 640px;
    height: 366px;
    border-radius: 26px;
    overflow: hidden;
    box-shadow: 0 14px 30px rgba(0,0,0,0.45);
  }
  /* Back side */
  .card--back {
    left: 60px;
    top: 60px;
    background: var(--card-dark);
  }
  .card--back .pattern-fill {
    position: absolute;
    inset: 0;
    background: linear-gradient(135deg, var(--card-dark) 0%, var(--card-dark-deep) 100%);
  }
  .card--back .back-brand {
    position: absolute;
    right: 46px;
    top: 150px;
    display: flex;
    align-items: center;
    gap: 10px;
    font-family: "Michroma", sans-serif;
    font-size: 18px;
    color: var(--accent);
    letter-spacing: 1px;
  }
  .brand-square {
    width: 16px;
    height: 16px;
    background: var(--accent);
  }
  /* Front side */
  .card--front {
    left: 500px;
    top: 478px;
    background: var(--card-light);
  }
  .person {
    position: absolute;
    left: 44px;
    top: 64px;
  }
  .person__name {
    font-family: "Michroma", sans-serif;
    font-size: 20px;
    color: var(--ink);
    letter-spacing: 1px;
    line-height: 1.2;
  }
  .person__title {
    font-family: "Michroma", sans-serif;
    font-size: 14px;
    color: var(--accent);
    letter-spacing: 1px;
    margin-top: 2px;
  }
  .brand {
    position: absolute;
    right: 40px;
    top: 110px;
    display: flex;
    align-items: center;
    gap: 12px;
    font-family: "Michroma", sans-serif;
    font-size: 22px;
    color: var(--ink);
    letter-spacing: 1px;
  }
  .brand .brand-square { background: var(--accent); width: 18px; height: 18px; }
  .contacts {
    position: absolute;
    left: 44px;
    bottom: 40px;
    list-style: none;
  }
  .contacts li {
    display: flex;
    align-items: center;
    gap: 12px;
    font-size: 17px;
    color: var(--muted);
    letter-spacing: 0.5px;
    line-height: 30px;
  }
  .contacts svg { width: 18px; height: 18px; flex: none; }
</style>
</head>
<body>

  <section class="card card--back" aria-label="Card back">
    <div class="pattern-fill" role="img" aria-label="Faint repeating brand pattern on dark grey"></div>
    <div class="back-brand"><span class="brand-square"></span>Valbrook Data Works</div>
  </section>

  <section class="card card--front" aria-label="Card front">
    <div class="person">
      <p class="person__name">MARCUS HALE</p>
      <p class="person__title">MANAGING DIRECTOR</p>
    </div>

    <div class="brand"><span class="brand-square"></span>Valbrook Data Works</div>

    <ul class="contacts">
      <li>
        <svg viewBox="0 0 24 24" aria-hidden="true"><path fill="#d9892a" d="M6.6 10.8a15.1 15.1 0 0 0 6.6 6.6l2.2-2.2c.3-.3.7-.4 1-.2 1.1.4 2.3.6 3.6.6.6 0 1 .4 1 1V20c0 .6-.4 1-1 1A17 17 0 0 1 3 4c0-.6.4-1 1-1h3.5c.6 0 1 .4 1 1 0 1.3.2 2.5.6 3.6.1.3 0 .7-.2 1z"/></svg>
        0917-4410-2286
      </li>
      <li>
        <svg viewBox="0 0 24 24" aria-hidden="true"><rect x="2" y="5" width="20" height="14" rx="1.5" fill="#d9892a"/><path d="M2.5 6l9.5 7 9.5-7" fill="none" stroke="#fff" stroke-width="1.6"/></svg>
        info@valbrookdataworks.com
      </li>
      <li>
        <svg viewBox="0 0 24 24" aria-hidden="true"><g fill="none" stroke="#d9892a" stroke-width="1.8"><circle cx="12" cy="12" r="9.5"/><ellipse cx="12" cy="12" rx="4" ry="9.5"/><path d="M2.5 12h19M4 7h16M4 17h16"/></g></svg>
        www.valbrookdataworks.com
      </li>
    </ul>
  </section>

</body>
</html>
```